MRHT Needs Fundraiser Dinner Invite!!

The Marisol Hendrick Trust, a 501 3(c) non for profit has a yearly fundraiser, with varying themes. Last year it was "cowboys" and "cowgirls"
This year, it is Club Orchid, or 70's disco music. I have uploaded last years invite for reference, some stock photography for inspiration. You are not limited to using the stock photos.

Annual MRHT Fundraiser Dinner
October 13th, 2022
Starts: 6:30pm
RSVP By: September 20th
Place: The Bramwell
Price: $135 per ticket

Target Market(s)

Donors, Business People, Every person

Industry/Entity Type

Non for Profit

Font styles to use
Sans Serif

Colors
0054AA
0677BA
7BADD7
CADEEF
E8F1F8
E54698
E96AAD
F1A4CE
F9D9EA
FCEFF6
6B429C
8869AF
B7A5CE
E3DAEB
F3F0F8

Requirements
Must have
• The invite should be 5x7, be sophisticated as the clientele are mainly business people that come to support the cause. It should be fun and inviting at the same time.

```html
<!DOCTYPE html>
<html lang="en">
<head>
<meta charset="utf-8">
<title>Annual MRHT Fundraiser Dinner</title>
<link rel="stylesheet" href="https://fonts.googleapis.com/css2?family=Monoton&family=Abril+Fatface&family=Archivo:wght@700&display=swap">
<style>
  :root {
    --ink-blue: #0d55a8;
    --sky: #c6d8ee;
    --mist: #e8eef8;
    --blush: #f1c6de;
    --lilac: #d7c9e4;
    --pink: #e96aad;
    --deep-pink: #e54698;
    --violet: #6b429c;
    --ocean: #0677ba;
  }
  html, body {
    margin: 0;
    padding: 0;
    width: 857px;
    height: 1200px;
    overflow: hidden;
    background: var(--sky);
  }
  .invite {
    display: block;
    width: 857px;
    height: 1200px;
  }
  .display-type {
    font-family: "Monoton", "Arial Black", sans-serif;
    fill: var(--ink-blue);
  }
  .serif-type {
    font-family: "Abril Fatface", "Georgia", serif;
    fill: var(--ink-blue);
  }
  .site-name {
    font-family: "Archivo", "Arial", sans-serif;
    font-weight: 700;
    fill: var(--pink);
  }
</style>
</head>
<body>
<svg class="invite" viewBox="0 0 857 1200" xmlns="http://www.w3.org/2000/svg">
  <defs>
    <radialGradient id="glow" cx="0.38" cy="0.3" r="0.75">
      <stop offset="0" stop-color="#f8eef5"/>
      <stop offset="0.5" stop-color="#dcdcee"/>
      <stop offset="1" stop-color="#c3d6ec"/>
    </radialGradient>
    <linearGradient id="ball" x1="0" y1="0" x2="1" y2="1">
      <stop offset="0" stop-color="#0677ba"/>
      <stop offset="0.55" stop-color="#7badd7"/>
      <stop offset="1" stop-color="#e8f1f8"/>
    </linearGradient>
    <linearGradient id="dancer" x1="0" y1="0" x2="0" y2="1">
      <stop offset="0" stop-color="#e3daeb"/>
      <stop offset="0.3" stop-color="#f1a4ce"/>
      <stop offset="0.55" stop-color="#b7a5ce"/>
      <stop offset="0.8" stop-color="#7badd7"/>
      <stop offset="1" stop-color="#0677ba"/>
    </linearGradient>
  </defs>

  <!-- backdrop -->
  <rect class="backdrop" width="857" height="1200" fill="url(#glow)"/>
  <g class="light-bands" opacity="0.45">
    <rect x="200" y="180" width="55" height="660" fill="var(--blush)"/>
    <rect x="295" y="180" width="60" height="660" fill="var(--lilac)"/>
    <rect x="390" y="180" width="55" height="660" fill="var(--blush)"/>
    <rect x="485" y="180" width="60" height="660" fill="var(--lilac)"/>
    <polygon points="200,840 255,840 80,1200 0,1200" fill="var(--blush)"/>
    <polygon points="295,840 355,840 300,1200 200,1200" fill="var(--lilac)"/>
    <polygon points="390,840 445,840 510,1200 410,1200" fill="var(--blush)"/>
    <polygon points="485,840 545,840 760,1200 650,1200" fill="var(--lilac)"/>
  </g>

  <!-- mirror ball -->
  <ellipse class="mirror-ball" role="img" aria-label="Illustration of a glowing blue disco mirror ball" cx="380" cy="-60" rx="262" ry="260" fill="url(#ball)"/>

  <!-- dancer illustration -->
  <polygon class="dancer-art" role="img" aria-label="Illustration of a 1970s disco dancer in a white suit and flared blue trousers pointing up, with vinyl records behind"
    points="560,250 740,240 845,310 850,1050 420,1050 470,720 545,470 560,380"
    fill="url(#dancer)" opacity="0.7"/>

  <!-- headline -->
  <text class="display-type headline" x="46" y="183" font-size="170" textLength="760" lengthAdjust="spacingAndGlyphs">ANNUAL</text>
  <text class="display-type headline" x="46" y="349" font-size="170" textLength="488" lengthAdjust="spacingAndGlyphs">MRHT</text>

  <!-- event details -->
  <text class="serif-type event-title" x="57" y="446" font-size="74" textLength="468" lengthAdjust="spacingAndGlyphs">Fundraiser</text>
  <text class="serif-type event-title" x="54" y="540" font-size="74" textLength="309" lengthAdjust="spacingAndGlyphs">Dinner</text>
  <text class="serif-type event-date" x="55" y="619" font-size="36" textLength="382" lengthAdjust="spacingAndGlyphs">October 13<tspan font-size="20" dy="-14">th</tspan><tspan dy="14">, 2022</tspan></text>
  <text class="serif-type event-time" x="55" y="664" font-size="36" textLength="302" lengthAdjust="spacingAndGlyphs">Starts: 6:30pm</text>

  <text class="display-type label" x="41" y="823" font-size="100" textLength="305" lengthAdjust="spacingAndGlyphs">RSVP</text>
  <text class="serif-type label-value" x="40" y="868" font-size="36" textLength="397" lengthAdjust="spacingAndGlyphs">By September 20<tspan font-size="20" dy="-14">th</tspan></text>

  <text class="display-type label" x="39" y="976" font-size="60" textLength="205" lengthAdjust="spacingAndGlyphs">PLACE</text>
  <text class="serif-type label-value" x="24" y="1023" font-size="38" textLength="291" lengthAdjust="spacingAndGlyphs">The Bramwell</text>

  <text class="display-type label" x="39" y="1104" font-size="60" textLength="192" lengthAdjust="spacingAndGlyphs">PRICE</text>
  <text class="serif-type label-value" x="38" y="1148" font-size="38" textLength="292" lengthAdjust="spacingAndGlyphs">$135 per ticket</text>

  <!-- site -->
  <circle class="site-dot" cx="458" cy="1113" r="26" fill="var(--pink)"/>
  <text class="site-name" x="523" y="1130" font-size="47" textLength="237" lengthAdjust="spacingAndGlyphs">MRHT.ORG</text>
</svg>
</body>
</html>
```